Everett's Book Cover

Need a cover design for a book (paperback and eBook)
Book Title: Where The Cedar Rivers Bend
Book Width: 15.24
Book Height: 22.86
Thickness: approximately 200 pages.
Book is a collection of stories drawn from the author's life, and will be in the local history genre in northern British Columbia, Canada from the period 1930 to the present time.
Author: Everett Hollis Pelletier
Must include "As told to Marnie Kowal" on front cover, not on the spine.
Author invites designers creativity and asks that the attached photos be incorporated into the front and back covers in tasteful ways as follows:
Other uses of the photos will be considered.
We apologize for the quality of the photos. Please do what you can.
We look forward to your designs.
Thank you for considering.

Target Market(s)

Lovers of local history, jokes, storytelling, back country hiking and mountain climbing. Men and women 30 years and older. Primary target readership are men and women in their 40's, 50's, 60's, and older, who love local history

Font styles to use
Sans Serif

Requirements
Must have
• Back cover copy must clear and easy to read.
Must appeal to outdoor, back country types.
Nice to have
• Like to see a creative incorporation of the photos provided.
Build on or compliment the colours in the photos

```html
<!DOCTYPE html>
<html lang="en">
<head>
<meta charset="utf-8">
<title>Where The Cedar Rivers Bend — Cover Spread</title>
<link rel="stylesheet" href="https://fonts.googleapis.com/css2?family=Marcellus&family=Marcellus+SC&family=EB+Garamond:wght@400;600&display=swap">
<style>
  :root {
    --page-bg: #ececec;
    --paper: #ffffff;
    --ink: #1b1b1b;
    --olive: #9b9562;
    --meadow: #7d8a4e;
    --mist: #c9d0c4;
    --illo-ochre: #a89a3a;
    --illo-rust: #9c5a34;
  }
  * { margin: 0; padding: 0; box-sizing: border-box; }
  html, body { width: 899px; height: 1200px; overflow: hidden; background: var(--page-bg); }
  .spread {
    position: absolute; left: 0; top: 292px;
    width: 899px; height: 616px;
    background: var(--paper);
    color: var(--ink);
  }
  /* back cover */
  .back-cover { position: absolute; left: 0; top: 0; width: 411px; height: 616px; overflow: hidden; }
  .back-copy {
    position: absolute; left: 45px; top: 56px; width: 330px;
    font-family: "EB Garamond", serif; font-size: 10.4px; line-height: 1.28;
    text-align: justify; z-index: 2;
  }
  .back-copy p + p { margin-top: 10px; }
  .back-copy .author-name { font-weight: 600; }
  .back-photo {
    position: absolute; left: 0; top: 250px; width: 411px; height: 366px;
    background:
      linear-gradient(to bottom, var(--paper) 0%, rgba(255,255,255,0.6) 25%, rgba(255,255,255,0) 55%),
      linear-gradient(to bottom, var(--mist) 0%, #8f9d78 45%, var(--meadow) 75%, #5d6a3a 100%);
  }
  .isbn-box {
    position: absolute; left: 266px; top: 505px; width: 102px; height: 68px;
    background: var(--paper); z-index: 2;
  }
  /* spine */
  .spine { position: absolute; left: 411px; top: 0; width: 64px; height: 616px; }
  .spine-title, .spine-author {
    position: absolute; left: 50%; white-space: nowrap;
    transform-origin: center; font-family: "Marcellus", serif;
  }
  .spine-title {
    top: 200px; font-size: 25px; letter-spacing: 0.5px;
    transform: translate(-50%, -50%) rotate(90deg);
  }
  .spine-title .accent { color: var(--olive); }
  .spine-author {
    top: 538px; font-family: "Marcellus SC", serif; font-size: 9.5px;
    transform: translate(-50%, -50%) rotate(90deg);
  }
  /* front cover */
  .front-cover { position: absolute; left: 475px; top: 0; width: 424px; height: 616px; text-align: center; }
  .title { font-family: "Marcellus", serif; font-weight: 400; }
  .title span { display: block; line-height: 1; }
  .title-line-1 { margin-top: 30px; font-size: 33px; }
  .title-line-2 { margin-top: 4px; font-size: 40px; letter-spacing: 0.5px; }
  .title-line-3 { margin-top: 2px; font-size: 62px; color: var(--olive); letter-spacing: 1px; }
  .as-told {
    margin-top: 8px; font-family: "Marcellus SC", serif; font-size: 11px;
    letter-spacing: 7px;
  }
  .illustration {
    position: absolute; left: 50%; top: 190px; transform: translateX(-50%);
    width: 300px; height: 330px;
  }
  .author-line {
    position: absolute; left: 0; right: 0; top: 593px;
    font-family: "Marcellus SC", serif; font-size: 17px; letter-spacing: 4px;
  }
</style>
</head>
<body>
  <main class="spread">
    <section class="back-cover">
      <div class="back-copy">
        <p><span class="author-name">Everett Pelletier</span> is a true old-fashioned story teller. He loves nothing better than a good story, and particularly when he is the one telling the story. He was born and raised in the tiny sawmill town of Larchmere, BC and spent 80 years of his life there before relocating to his current home on the banks of the Tsalkwa River in Fort Ardley, BC. In addition to writing this book, Everett spends his time writing songs, singing, telling jokes, and entertaining his many friends with stories of days gone by.<br>
        At the age of 15 he started his career as a flunky in the cookhouse, then moved on to work as a horse logger, sawmill worker, bush foreman, rancher, cat skinner, forest warden, road and bridge builder, and finished his career as salmon hatchery manager.</p>
        <p>Everett's love of the mountains is evident throughout the book, as is his love for the majestic grizzly bears who inhabit them. He spent his spare time mountain climbing, fishing, skiing, snowshoeing, and hiking in the woods near his home. This book is an eclectic collection of stories about family, friends, and adventures, all sprinkled with the author's unique sense of humour.</p>
      </div>
      <div class="back-photo" role="img" aria-label="Photo of the author and a companion standing in an alpine meadow with wildflowers, misty green mountain slopes and a snow patch behind them"></div>
      <div class="isbn-box"></div>
    </section>

    <section class="spine">
      <div class="spine-title">Where The Cedar <span class="accent">Rivers Bend</span></div>
      <div class="spine-author">Everett Hollis Pelletier</div>
    </section>

    <section class="front-cover">
      <h1 class="title">
        <span class="title-line-1">Where The</span>
        <span class="title-line-2">CEDAR RIVERS</span>
        <span class="title-line-3">BEND</span>
      </h1>
      <p class="as-told">As told to Marnie Kowal</p>
      <svg class="illustration" viewBox="0 0 300 330" role="img" aria-label="Sketched painting of a hiker with a pack and rifle striding inside a loose hand-drawn ring filled with golden meadow tones">
        <defs>
          <radialGradient id="illo-fill" cx="50%" cy="55%" r="50%">
            <stop offset="0%" stop-color="#c4b548"/>
            <stop offset="70%" stop-color="var(--illo-ochre)"/>
            <stop offset="100%" stop-color="#8a7d33"/>
          </radialGradient>
        </defs>
        <circle cx="150" cy="180" r="138" fill="url(#illo-fill)" opacity="0.85"/>
        <circle cx="150" cy="180" r="142" fill="none" stroke="#b9b3a3" stroke-width="4"/>
      </svg>
      <div class="author-line">Everett Hollis Pelletier</div>
    </section>
  </main>
</body>
</html>
```